Quality Improvement Software for healthcare agencies needs a website.

Veltrix820 is a software for hospices and home health agencies to manage their Quality Assurance Performance Improvement programs to remain complaint with the standards set by Sanovia and the Bureau of Civic Wellbeing. The web accessible software-as-a-service provides an easy, turn-key way for agencies to organize all the information they need to manage and track.

Coded - Design and coding required

4 page

```html
<!DOCTYPE html>
<html lang="en">
<head>
<meta charset="utf-8">
<title>Veltrix820 – Data Analytics</title>
<link href="https://fonts.googleapis.com/css2?family=Montserrat:wght@500;700&family=Roboto:wght@400;500;700&display=swap" rel="stylesheet">
<style>
:root{
  --magenta:#e6079a;
  --magenta-deep:#b80a7d;
  --black:#000;
  --ink:#111;
  --white:#fff;
  --grey-ph:#d9d9d9;
  --grey-icon:#bdbdbd;
  --blush:#f8e1e3;
  --cta-grey:#dadada;
}
*{box-sizing:border-box;margin:0;padding:0}
html,body{width:1200px;height:3958px;overflow:hidden}
body{font-family:"Roboto",sans-serif;color:var(--ink);background:var(--white);position:relative}
.abs{position:absolute}
section,header,footer{position:absolute;left:0;width:1200px;overflow:hidden}
a{color:inherit;text-decoration:none}

/* header */
.site-header{top:0;height:101px;background:var(--white)}
.brand{left:120px;top:50px;transform:translateY(-50%);display:flex;align-items:center;gap:10px;font:700 20px "Roboto",sans-serif;color:var(--ink)}
.brand-dot{width:16px;height:16px;border-radius:50%;background:var(--magenta)}
.nav-link{top:59px;font:500 12px "Roboto",sans-serif;color:#333}
.slant{position:absolute;display:flex;align-items:center;justify-content:center;font:500 12px "Roboto",sans-serif}
.slant svg{position:absolute;inset:0;width:100%;height:100%}
.slant span{position:relative}

/* hero */
.hero{top:101px;height:645px;background:linear-gradient(160deg,#1b2230,#0b0f16 60%,#141a24)}
.hero-title{left:88px;top:199px;font:500 43px/1.1 "Montserrat",sans-serif;color:var(--white)}
.hero-title em{font-style:normal;font-weight:700;color:var(--magenta)}
.hero-title u{text-decoration:none;border-bottom:3px solid var(--white);padding-bottom:1px}
.hero-text{left:92px;top:314px;width:380px;font:400 14px/1.45 "Roboto",sans-serif;color:var(--white)}

/* about */
.about{top:746px;height:646px;background:radial-gradient(circle at 30% 40%,#c93a6c 0,#7a2a7a 30%,#35184e 60%,#1a0f2a 100%)}
.about-title{left:600px;top:166px;font:700 43px "Montserrat",sans-serif;color:var(--white)}
.about-text{left:600px;top:236px;width:360px;font:400 13px/1.5 "Roboto",sans-serif;color:var(--white)}

/* stories */
.stories-head{top:1392px;height:252px;background:var(--black);color:var(--white)}
.eyebrow{width:100%;text-align:center;font:500 11px "Roboto",sans-serif}
.section-title{width:100%;text-align:center;font:700 40px "Roboto",sans-serif}
.rule{height:3px;background:var(--magenta)}
.tab{top:170px;font:400 12px "Roboto",sans-serif;color:var(--white)}

.stories{top:1644px;height:863px;background:var(--white)}
.story-card{width:494px;height:315px;background:var(--white);box-shadow:0 2px 6px rgba(0,0,0,.22)}
.story-bar{left:494px;top:0;width:19px;height:300px;background:var(--magenta)}
.ph{background:var(--grey-ph);display:flex;align-items:center;justify-content:center}
.ph svg{width:62px;height:50px}
.story-img{left:38px;top:41px;width:209px;height:227px}
.story-title{left:276px;top:58px;width:190px;font:700 18px/26px "Roboto",sans-serif}
.story-text{left:276px;top:142px;width:180px;padding-left:8px;border-left:2px solid var(--magenta);font:400 12px/18px "Roboto",sans-serif}
.author{display:flex;align-items:center;gap:14px;font:400 10px/16px "Roboto",sans-serif}
.author b{font-weight:700;display:block}
.avatar{width:34px;height:34px;border-radius:50%;background:var(--grey-ph);display:flex;align-items:center;justify-content:center}
.avatar i{width:13px;height:10px;border:2px solid var(--grey-icon);border-radius:2px}

/* latest */
.latest{top:2507px;height:700px;background:var(--black)}
.latest-title{width:100%;text-align:center;top:118px;font:500 36px "Roboto",sans-serif}
.latest-sub{width:100%;text-align:center;top:162px;font:400 13px "Roboto",sans-serif}
.post{width:347px}
.post-img{position:absolute;left:0;top:0;width:347px;height:226px}
.post-tag{top:250px;font:700 10px "Roboto",sans-serif}
.post-title{top:270px;font:500 18px "Roboto",sans-serif}
.post-text{top:302px;width:340px;font:400 12px/18px "Roboto",sans-serif;color:#222}
.post .author{top:357px}
.btn-outline{left:559px;top:633px;width:80px;height:35px;border:1px solid #333;display:flex;align-items:center;justify-content:center;font:400 12px "Roboto",sans-serif}

/* cta */
.cta{top:3207px;height:295px;background:var(--cta-grey)}
.cta-title{left:54px;top:92px;width:520px;font:700 30px/36px "Roboto",sans-serif;color:var(--white)}
.cta-text{left:54px;top:195px;font:400 13px "Roboto",sans-serif;color:var(--white)}

/* footer */
.site-footer{top:3502px;height:456px;background:var(--black);color:var(--white)}
.foot-logo{left:48px;top:62px;font:700 20px "Roboto",sans-serif}
.foot-col{top:69px;font:400 11px "Roboto",sans-serif}
.foot-col h4{font:500 11px "Roboto",sans-serif;margin-bottom:22px}
.foot-col li{list-style:none;height:28px}
.email-input{left:768px;top:127px;width:278px;height:37px;background:var(--white);color:var(--magenta);font:400 12px "Roboto",sans-serif;display:flex;align-items:center;padding-left:10px}
.email-btn{left:1057px;top:127px;width:91px;height:37px;border:1px solid var(--white);display:flex;align-items:center;justify-content:center;font:400 12px "Roboto",sans-serif}
.email-note{left:768px;top:178px;font:400 9px "Roboto",sans-serif}
.foot-rule{left:48px;top:310px;width:1100px;height:1px;background:#666}
.legal{top:338px;font:400 10px "Roboto",sans-serif}
.legal.u{text-decoration:underline}
.social{top:338px;width:14px;height:14px;background:var(--white);border-radius:3px}
</style>
</head>
<body>

<header class="site-header">
  <svg class="abs" style="left:0;top:0" width="800" height="31"><polygon points="0,0 800,0 722,31 0,31" fill="var(--magenta)"/></svg>
  <div class="abs brand"><span class="brand-dot"></span>Veltrix820</div>
  <a class="abs nav-link" style="left:436px">Home</a>
  <a class="abs nav-link" style="left:516px">About us</a>
  <a class="slant" style="left:587px;top:57px;width:76px;height:20px;color:#333"><svg viewBox="0 0 76 20" preserveAspectRatio="none"><polygon points="8,1 75,1 68,19 1,19" fill="none" stroke="var(--magenta)" stroke-width="1.2"/></svg><span>Services</span></a>
  <a class="abs nav-link" style="left:682px">Case Studios</a>
  <a class="abs nav-link" style="left:791px">Blog</a>
  <a class="slant" style="left:894px;top:55px;width:104px;height:22px;color:#333"><svg viewBox="0 0 104 22" preserveAspectRatio="none"><polygon points="9,1 103,1 95,21 1,21" fill="none" stroke="var(--magenta)" stroke-width="1.2"/></svg><span>How it Works</span></a>
  <a class="slant" style="left:1012px;top:55px;width:104px;height:22px;color:var(--white)"><svg viewBox="0 0 104 22" preserveAspectRatio="none"><polygon points="9,0 104,0 95,22 0,22" fill="var(--black)"/></svg><span>Contact us</span></a>
</header>

<section class="hero">
  <svg class="abs" style="left:0;top:0" width="1200" height="645">
    <polygon points="445,0 475,0 752,262 506,645 476,645 722,262" fill="var(--magenta)"/>
    <polygon points="490,0 1200,0 1200,645 520,645 735,262" fill="#e9edf1" role="img" aria-label="Photo of healthcare staff walking down a bright hospital corridor"/>
    <polygon points="528,645 1200,545 1200,645" fill="var(--white)"/>
  </svg>
  <h1 class="abs hero-title">Unlock the Power<br><em>of <u>Data</u> Analytics</em></h1>
  <p class="abs hero-text">We provide cutting-edge data analytics solutions to help businesses make informed decisions and drive growth.</p>
  <a class="slant" style="left:77px;top:369px;width:107px;height:23px;color:var(--white)"><svg viewBox="0 0 107 23" preserveAspectRatio="none"><polygon points="10,1 106,1 97,22 1,22" fill="none" stroke="var(--magenta)" stroke-width="1.2"/></svg><span>How it Works</span></a>
  <a class="slant" style="left:195px;top:369px;width:101px;height:23px;color:var(--white)"><svg viewBox="0 0 101 23" preserveAspectRatio="none"><polygon points="10,0 101,0 91,23 0,23" fill="var(--magenta)"/></svg><span>Contact us</span></a>
</section>

<section class="about" role="img" aria-label="Abstract image of glowing purple and red neural filaments">
  <svg class="abs" style="left:0;top:0" width="1200" height="646"><polygon points="512,0 1200,0 1200,602 512,528" fill="var(--magenta-deep)"/></svg>
  <h2 class="abs about-title">About Us</h2>
  <p class="abs about-text">We provide cutting-edge data analytics solutions to help businesses make informed decisions and drive growth.</p>
  <a class="slant" style="left:590px;top:293px;width:104px;height:21px;color:var(--white)"><svg viewBox="0 0 104 21" preserveAspectRatio="none"><polygon points="9,1 103,1 95,20 1,20" fill="none" stroke="var(--white)" stroke-width="1.2"/></svg><span>How it Works</span></a>
  <a class="slant" style="left:707px;top:293px;width:103px;height:21px;color:#fbd3ec"><svg viewBox="0 0 103 21" preserveAspectRatio="none"><polygon points="5,0 103,0 98,21 0,21" fill="#f6c9e6"/></svg><span>Contact us</span></a>
</section>

<section class="stories-head">
  <p class="abs eyebrow" style="top:73px">Articles</p>
  <h2 class="abs section-title" style="top:94px">Recent Success Stories</h2>
  <div class="abs rule" style="left:0;top:121px;width:353px"></div>
  <div class="abs rule" style="left:846px;top:127px;width:349px"></div>
  <a class="slant" style="left:403px;top:167px;width:89px;height:23px;color:var(--white)"><svg viewBox="0 0 89 23" preserveAspectRatio="none"><polygon points="9,1 88,1 80,22 1,22" fill="none" stroke="var(--magenta)" stroke-width="1.2"/></svg><span>View all</span></a>
  <a class="abs tab" style="left:511px">Financial</a>
  <a class="abs tab" style="left:579px">Technology</a>
  <a class="abs tab" style="left:658px">Healthcare</a>
  <a class="abs tab" style="left:734px">Retail</a>
</section>

<section class="stories">
  <article class="abs story-card" style="left:54px;top:77px">
    <div class="abs story-bar"></div>
    <div class="abs ph story-img" role="img" aria-label="Story image"><svg viewBox="0 0 62 50"><rect width="62" height="50" rx="6" fill="var(--grey-icon)"/><circle cx="44" cy="15" r="5" fill="var(--grey-ph)"/><polygon points="8,42 24,22 36,36 42,30 54,42" fill="var(--grey-ph)"/></svg></div>
    <h3 class="abs story-title">Unlocking Data Insights for Business Growth</h3>
    <p class="abs story-text">Learn how our data analytics solutions have helped companies achieve success.</p>
    <div class="abs author" style="left:276px;top:218px"><span class="avatar"><i></i></span><div><b>John Doe</b>11 Jan 2022 &nbsp;•&nbsp; 5 min read</div></div>
  </article>
  <article class="abs story-card" style="left:616px;top:77px">
    <div class="abs story-bar"></div>
    <div class="abs ph story-img" role="img" aria-label="Story image"><svg viewBox="0 0 62 50"><rect width="62" height="50" rx="6" fill="var(--grey-icon)"/><circle cx="44" cy="15" r="5" fill="var(--grey-ph)"/><polygon points="8,42 24,22 36,36 42,30 54,42" fill="var(--grey-ph)"/></svg></div>
    <h3 class="abs story-title">Unlocking Data Insights for Business Growth</h3>
    <p class="abs story-text">Learn how our data analytics solutions have helped companies achieve success.</p>
    <div class="abs author" style="left:276px;top:218px"><span class="avatar"><i></i></span><div><b>John Doe</b>11 Jan 2022 &nbsp;•&nbsp; 5 min read</div></div>
  </article>
  <article class="abs story-card" style="left:54px;top:473px">
    <div class="abs story-bar"></div>
    <div class="abs ph story-img" role="img" aria-label="Story image"><svg viewBox="0 0 62 50"><rect width="62" height="50" rx="6" fill="var(--grey-icon)"/><circle cx="44" cy="15" r="5" fill="var(--grey-ph)"/><polygon points="8,42 24,22 36,36 42,30 54,42" fill="var(--grey-ph)"/></svg></div>
    <h3 class="abs story-title">Unlocking Data Insights for Business Growth</h3>
    <p class="abs story-text">Learn how our data analytics solutions have helped companies achieve success.</p>
    <div class="abs author" style="left:276px;top:218px"><span class="avatar"><i></i></span><div><b>John Doe</b>11 Jan 2022 &nbsp;•&nbsp; 5 min read</div></div>
  </article>
  <article class="abs story-card" style="left:616px;top:473px">
    <div class="abs story-bar"></div>
    <div class="abs ph story-img" role="img" aria-label="Story image"><svg viewBox="0 0 62 50"><rect width="62" height="50" rx="6" fill="var(--grey-icon)"/><circle cx="44" cy="15" r="5" fill="var(--grey-ph)"/><polygon points="8,42 24,22 36,36 42,30 54,42" fill="var(--grey-ph)"/></svg></div>
    <h3 class="abs story-title">Unlocking Data Insights for Business Growth</h3>
    <p class="abs story-text">Learn how our data analytics solutions have helped companies achieve success.</p>
    <div class="abs author" style="left:276px;top:218px"><span class="avatar"><i></i></span><div><b>John Doe</b>11 Jan 2022 &nbsp;•&nbsp; 5 min read</div></div>
  </article>
</section>

<section class="latest">
  <svg class="abs" style="left:0;top:0" width="1200" height="700">
    <polygon points="95,74 1088,74 1160,151 1200,151 1200,700 0,700 0,151 40,151" fill="var(--white)"/>
    <polygon points="1200,220 1200,700 327,700" fill="var(--blush)"/>
  </svg>
  <p class="abs eyebrow" style="top:94px">Latest</p>
  <h2 class="abs latest-title">Stay Informed with Analytics</h2>
  <p class="abs latest-sub">Discover the latest articles and insights on data analytics trends.</p>

  <article class="abs post" style="left:54px;top:224px">
    <div class="ph post-img" role="img" aria-label="Article image"><svg viewBox="0 0 62 50"><rect width="62" height="50" rx="6" fill="var(--grey-icon)"/><circle cx="44" cy="15" r="5" fill="var(--grey-ph)"/><polygon points="8,42 24,22 36,36 42,30 54,42" fill="var(--grey-ph)"/></svg></div>
    <p class="abs post-tag">Trends</p>
    <h3 class="abs post-title">Unlocking the Power of Data Analytics</h3>
    <p class="abs post-text">Learn how data analytics can drive business growth and innovation.</p>
    <div class="abs author"><span class="avatar"><i></i></span><div><b>John Doe</b>11 Jan 2022 &nbsp;•&nbsp; 5 min read</div></div>
  </article>
  <article class="abs post" style="left:425px;top:224px">
    <div class="ph post-img" role="img" aria-label="Article image"><svg viewBox="0 0 62 50"><rect width="62" height="50" rx="6" fill="var(--grey-icon)"/><circle cx="44" cy="15" r="5" fill="var(--grey-ph)"/><polygon points="8,42 24,22 36,36 42,30 54,42" fill="var(--grey-ph)"/></svg></div>
    <p class="abs post-tag">Technology</p>
    <h3 class="abs post-title">The Future of Data Analytics</h3>
    <p class="abs post-text">Exploring the latest advancements and trends in data analytics.</p>
    <div class="abs author" style="top:333px"><span class="avatar"><i></i></span><div><b>Jane Smith</b>11 Jan 2022 &nbsp;•&nbsp; 5 min read</div></div>
  </article>
  <article class="abs post" style="left:797px;top:224px">
    <div class="ph post-img" role="img" aria-label="Article image"><svg viewBox="0 0 62 50"><rect width="62" height="50" rx="6" fill="var(--grey-icon)"/><circle cx="44" cy="15" r="5" fill="var(--grey-ph)"/><polygon points="8,42 24,22 36,36 42,30 54,42" fill="var(--grey-ph)"/></svg></div>
    <p class="abs post-tag">Business</p>
    <h3 class="abs post-title">Data Analytics Strategies for Success</h3>
    <p class="abs post-text">Discover effective strategies for leveraging data analytics in your business.</p>
    <div class="abs author"><span class="avatar"><i></i></span><div><b>David Lee</b>11 Jan 2022 &nbsp;•&nbsp; 5 min read</div></div>
  </article>
  <a class="abs btn-outline">Button</a>
</section>

<section class="cta">
  <svg class="abs" style="left:0;top:0" width="700" height="295"><polygon points="0,0 519,0 696,164 492,295 0,295" fill="var(--magenta)"/></svg>
  <h2 class="abs cta-title">Transforming Data into Actionable Insights</h2>
  <p class="abs cta-text">Unlock the Power of Your Data with Our Analytics Services</p>
</section>

<footer class="site-footer">
  <p class="abs foot-logo">Logo</p>
  <div class="abs foot-col" style="left:212px"><h4>About Us</h4><ul><li>Services</li><li>Products</li><li>Case Studies</li><li>Blog</li><li>Contact</li></ul></div>
  <div class="abs foot-col" style="left:375px"><h4>Careers</h4><ul><li>Support</li><li>FAQ</li><li>Login/Register</li><li>Link One</li><li>Link Two</li></ul></div>
  <div class="abs foot-col" style="left:539px"><h4>Link Three</h4><ul><li>Link Four</li><li>Link Five</li><li>Link Six</li><li>Link Seven</li><li>Link Eight</li></ul></div>
  <div class="abs foot-col" style="left:770px"><h4 style="margin-bottom:14px">Link Nine</h4><ul><li>Link Ten</li></ul></div>
  <div class="abs email-input">Placeholder</div>
  <div class="abs email-btn">Button</div>
  <p class="abs email-note">Enter email address</p>
  <div class="abs foot-rule"></div>
  <p class="abs legal" style="left:48px">Thank you! Your subscription has been confirmed.</p>
  <p class="abs legal u" style="left:302px">Oops! Something went wrong. Please try again later.</p>
  <p class="abs legal u" style="left:565px">© 2023 Northlane. All rights reserved.</p>
  <p class="abs legal u" style="left:750px">Privacy Policy</p>
  <span class="abs social" style="left:1023px;border-radius:50%"></span>
  <span class="abs social" style="left:1050px"></span>
  <span class="abs social" style="left:1077px"></span>
  <span class="abs social" style="left:1104px"></span>
  <span class="abs social" style="left:1131px"></span>
</footer>

</body>
</html>
```